Potential SF Gazette Best Seller Poetry Book Cover Contest

I’m penning my first poetry book. It’s entitled “Lanterns Under Rain”
I’m fairly open to creative freedom but I want the cover to without a doubt catch a persons' eye instantly because first impressions are VERY IMPORTANT in the literary world
I tend to lean towards a luxury look and colors like black, gold, rose gold, silver, glitter etc but again I’m open to interpretation
Looking forward to your submissions
Target Market(s)
those seeking relatable love advice and quotes
modern millenials
Colors
Look and feel

```html
<!DOCTYPE html>
<html lang="en">
<head>
<meta charset="utf-8">
<title>Lanterns Under Rain — Book Cover</title>
<link href="https://fonts.googleapis.com/css2?family=Jost:wght@400&family=Kaushan+Script&display=swap" rel="stylesheet">
<style>
  :root {
    --backdrop: #e6e6e6;
    --cover-black: #050505;
    --title-red: #c8161d;
    --title-red-deep: #8e0f14;
    --gold-light: #f6c51c;
    --gold-deep: #b07d0a;
    --ink-white: #ffffff;
    --subtitle: #e8e8e8;
  }
  html, body {
    margin: 0;
    padding: 0;
    width: 1200px;
    height: 1000px;
    overflow: hidden;
    background: var(--backdrop);
  }
  .stage {
    position: relative;
    width: 1200px;
    height: 1000px;
  }
  .cover {
    position: absolute;
    left: 295px;
    top: 10px;
    width: 650px;
    height: 975px;
    background: var(--cover-black);
    overflow: hidden;
  }
  .glitter-field {
    position: absolute;
    left: 0;
    top: 230px;
    width: 650px;
    height: 480px;
    background: radial-gradient(ellipse 48% 46% at 50% 52%,
      rgba(214, 165, 20, 0.38) 0%,
      rgba(180, 130, 10, 0.22) 45%,
      rgba(120, 85, 5, 0.08) 75%,
      rgba(0, 0, 0, 0) 100%);
  }
  .title {
    position: absolute;
    inset: 0;
    margin: 0;
    font-weight: normal;
  }
  .title-lead {
    position: absolute;
    right: 262px;
    top: 128px;
    font-family: "Kaushan Script", cursive;
    font-size: 52px;
    line-height: 1;
    color: var(--ink-white);
    white-space: nowrap;
  }
  .heart-icon {
    position: absolute;
    left: 405px;
    top: 140px;
    width: 112px;
    height: 96px;
    z-index: 2;
  }
  .title-main {
    position: absolute;
    left: 43px;
    top: 200px;
    width: 600px;
    text-align: center;
    font-family: "Jost", sans-serif;
    font-weight: 400;
    font-size: 128px;
    line-height: 1;
    letter-spacing: 0;
    white-space: nowrap;
    background: linear-gradient(90deg, var(--title-red-deep), var(--title-red) 30%, var(--title-red) 70%, var(--title-red-deep));
    -webkit-background-clip: text;
    background-clip: text;
    color: transparent;
  }
  .title-accent {
    position: absolute;
    left: 0;
    top: 320px;
    width: 650px;
    text-align center;
    text-align: center;
    font-family: "Kaushan Script", cursive;
    font-size: 210px;
    line-height: 1.2;
    white-space: nowrap;
    background: linear-gradient(90deg, var(--gold-deep), var(--gold-light) 35%, var(--gold-light) 65%, var(--gold-deep));
    -webkit-background-clip: text;
    background-clip: text;
    color: transparent;
  }
  .subtitle {
    position: absolute;
    left: 0;
    top: 836px;
    width: 650px;
    margin: 0;
    text-align: center;
    font-family: "Jost", sans-serif;
    font-size: 14px;
    line-height: 24px;
    letter-spacing: 2.6px;
    color: var(--subtitle);
  }
</style>
</head>
<body>
  <main class="stage">
    <section class="cover" aria-label="Book cover: Lanterns Under Rain">
      <div class="glitter-field" role="img" aria-label="Spray of fine gold glitter behind the title"></div>
      <h1 class="title">
        <span class="title-lead">Lanterns</span>
        <span class="title-main">UNDER</span>
        <span class="title-accent">Rain</span>
      </h1>
      <svg class="heart-icon" viewBox="0 0 112 96" aria-hidden="true">
        <defs>
          <radialGradient id="heartFill" cx="45%" cy="35%" r="70%">
            <stop offset="0%" stop-color="#e8343a"/>
            <stop offset="60%" stop-color="#c3141b"/>
            <stop offset="100%" stop-color="#7d0a0e"/>
          </radialGradient>
        </defs>
        <path d="M56 92 C20 66 2 46 2 27 C2 12 14 2 29 2 C41 2 51 9 56 19 C61 9 71 2 83 2 C98 2 110 12 110 27 C110 46 92 66 56 92 Z" fill="url(#heartFill)"/>
        <path d="M14 30 C14 18 24 12 34 12 C44 12 50 18 56 26 C62 18 70 12 80 12 C92 12 100 20 98 30 C80 22 40 40 14 30 Z" fill="#ffffff" opacity="0.35"/>
      </svg>
      <p class="subtitle">THOSE SEEKING RELATABLE LOVE ADVICE AND<br>QUOTES MODERN MILLENIALS</p>
    </section>
  </main>
</body>
</html>
```